Equipment Finance Specialist I work with companies who need the funds to buy their equipment

I would like a business card that stands out on the shelves. I want to be able to hand it to someone and say WOW. This card should have my logo.
You can put color into it I am very open on design and color

What my company does is we deal with dealerships that sell equipment such as Dump Trucks garbage trucks tractors trailers. Customers get referred to us and depending on their time in business we will ask for the following items

Companies that have been in business for more than two years we have a credit application program up to 250K . With this program we need the following items Credit application filled out(which is what I would like to be able for the customer to click on my website to get.) as well as three current month bank statements.

Deals over 250k we will need the following items

2 years business tax returns
2 years personal tax returns
Profit & Loss statement
Personal Financial Statement

what we do
100% FINANCING
SEASONAL PAYMENTS
LOAN BALLOON PAYMENTS
TRAC LEASING
LOW-INTEREST REFINANCING RATES
DEBT CONSOLIDATION

We specialize in creative financing solutions and offer a variety of reliable, flexible and expandable lending choices.

Target Market(s)

Trucking Companies

Industry/Entity Type

Trucking Company

Contact Information for Business Card

* $250,000 Application only Program
* Loans from $30,000 to 5,000,000
* Competitive Interest Rates

Font styles to use
Serif
Sans Serif

Colors

Designer to choose colors to be used in the design.

Requirements
Must have
• On the back of the card.
• * $250,000 Application only Program
• * Loans from $30,000 to 5,000,000
• My name, email, website. address
• * Competitive Interest Rates
• * 100% Financing
Nice to have
• I want my logo to pop on the card
• My logo is the great one I would like to use
Should not have
• I am up for your creativity as well

```html
<!DOCTYPE html>
<html lang="en">
<head>
<meta charset="utf-8">
<title>Ridgeline Lending – Business Card</title>
<link rel="stylesheet" href="https://fonts.googleapis.com/css2?family=Exo+2:wght@700;800&family=Roboto:wght@400;500&display=swap">
<style>
  :root {
    --navy: #1f2a68;
    --navy-deep: #18205a;
    --red: #e0202f;
    --white: #ffffff;
    --paper: #f4f4f6;
    --silver: #d9dde4;
    --ghost: #e6e8f0;
    --backdrop: #ecebe8;
  }
  * { box-sizing: border-box; margin: 0; padding: 0; }
  html, body { width: 900px; height: 1200px; overflow: hidden; }
  body {
    background: var(--backdrop);
    position: relative;
    font-family: "Roboto", Arial, sans-serif;
    color: var(--navy);
  }
  .card {
    position: absolute;
    left: 82px;
    width: 740px;
    height: 432px;
    overflow: hidden;
    box-shadow: 0 8px 18px rgba(0,0,0,.18);
  }

  /* Front */
  .card--front {
    top: 125px;
    background: linear-gradient(180deg, var(--white), var(--paper));
    border-radius: 42px 0 42px 0;
  }
  .front__wordmark {
    position: absolute; left: 48px; top: 200px; top: 78px;
    display: flex; align-items: center; gap: 12px;
    font-family: "Exo 2", sans-serif; font-weight: 800;
    font-size: 34px; color: var(--navy); text-transform: uppercase;
  }
  .wordmark__dot {
    width: 26px; height: 26px; border-radius: 50%; background: var(--red);
  }
  .front__decor {
    position: absolute; left: 352px; top: 30px;
    width: 378px; height: 330px; border-radius: 50%;
    background: radial-gradient(circle at 55% 50%, var(--ghost), rgba(230,232,240,0) 70%);
  }
  .front__features {
    position: absolute; right: 56px; top: 62px;
    list-style: none; text-align: right;
    font-size: 16.5px; line-height: 22.5px; font-weight: 500;
  }
  .front__features li::after {
    content: ""; display: inline-block; width: 8px; height: 8px;
    margin-left: 9px; background: var(--red); vertical-align: 1px;
  }
  .front__person { position: absolute; left: 48px; top: 240px; }
  .person__name {
    font-family: "Exo 2", sans-serif; font-weight: 800; font-size: 21px;
    letter-spacing: .5px; text-transform: uppercase;
  }
  .person__title {
    font-family: "Exo 2", sans-serif; font-weight: 700; font-size: 16px;
    color: var(--red); text-transform: uppercase;
  }
  .front__rule {
    position: absolute; left: 48px; right: 56px; top: 296px; height: 2px;
    background: linear-gradient(90deg, var(--navy) 0 50%, var(--red) 50% 100%);
  }
  .front__contact {
    position: absolute; left: 48px; top: 312px;
    list-style: none; font-size: 16.5px; line-height: 23px;
  }
  .front__contact li { display: flex; align-items: center; gap: 10px; }
  .front__contact svg { width: 17px; height: 17px; }
  .front__address {
    position: absolute; right: 56px; top: 312px;
    font-style: normal; text-align: right; font-size: 16.5px; line-height: 23px;
  }
  .front__band {
    position: absolute; left: 0; right: 0; bottom: 0; height: 49px;
    background: linear-gradient(180deg, #2c3a86, var(--navy-deep));
    border-top: 3px solid var(--silver);
    display: flex; align-items: center; justify-content: center;
    font-family: "Exo 2", sans-serif; font-weight: 800; font-size: 17px;
    letter-spacing: 1px; color: var(--white);
  }

  /* Back */
  .card--back {
    top: 643px;
    background: radial-gradient(ellipse at 50% 45%, #34439a, var(--navy-deep) 75%);
    border-radius: 0 42px 0 42px;
  }
  .back__wordmark {
    position: absolute; left: 0; right: 0; top: 168px;
    display: flex; align-items: center; justify-content: center; gap: 16px;
    font-family: "Exo 2", sans-serif; font-weight: 800;
    font-size: 50px; color: var(--white); text-transform: uppercase;
  }
  .back__wordmark .wordmark__dot { width: 38px; height: 38px; }
  .back__band {
    position: absolute; left: 0; right: 0; top: 374px; height: 30px;
    background: linear-gradient(180deg, #f5f6f8, var(--silver));
    display: flex; align-items: center; justify-content: center;
    font-family: "Exo 2", sans-serif; font-weight: 800; font-size: 17px;
    letter-spacing: 1px; color: #1a1a1a;
  }
  .back__stripes {
    position: absolute; left: 648px; top: 374px; height: 30px;
    display: flex; gap: 10px;
  }
  .back__stripes span { width: 8px; background: var(--red); }
</style>
</head>
<body>
  <section class="card card--front">
    <div class="front__decor" role="img" aria-label="Faint large truck illustration in a circular swoosh"></div>
    <div class="front__wordmark"><span class="wordmark__dot"></span>Ridgeline Lending</div>
    <ul class="front__features">
      <li>$250,000 Application only Program</li>
      <li>Loans from $30,000 to 5,000,000</li>
      <li>Competitive Interest Rates</li>
      <li>100% Financing</li>
    </ul>
    <div class="front__person">
      <p class="person__name">Daniel Morrow</p>
      <p class="person__title">CEO/Founder</p>
    </div>
    <div class="front__rule"></div>
    <ul class="front__contact">
      <li>
        <svg viewBox="0 0 24 24" aria-hidden="true"><path fill="#e0202f" d="M6.6 10.8a15.1 15.1 0 0 0 6.6 6.6l2.2-2.2c.3-.3.7-.4 1-.2 1.1.4 2.3.6 3.6.6.6 0 1 .4 1 1V20c0 .6-.4 1-1 1A17 17 0 0 1 3 4c0-.6.4-1 1-1h3.5c.6 0 1 .4 1 1 0 1.3.2 2.5.6 3.6.1.3 0 .7-.2 1z"/></svg>
        351-220-415-086
      </li>
      <li>
        <svg viewBox="0 0 24 24" aria-hidden="true"><rect x="2" y="5" width="20" height="14" fill="#e0202f"/><path d="M2 5l10 8 10-8" stroke="#fff" stroke-width="1.8" fill="none"/></svg>
        daniel@ridgelinelending.com
      </li>
    </ul>
    <address class="front__address">Rua das Oliveiras, 148<br>4400-052, Porto Sul</address>
    <div class="front__band">WWW.RIDGELINELENDING.COM</div>
  </section>

  <section class="card card--back">
    <div class="back__wordmark"><span class="wordmark__dot"></span>Ridgeline Lending</div>
    <div class="back__band">WWW.RIDGELINELENDING.COM</div>
    <div class="back__stripes"><span></span><span></span></div>
  </section>
</body>
</html>
```